The Gemstone Craft Studio Sales Business Card

The goal of this project is to create a interactive & effective business card design for SALES purposes with the intention to get customer on to our website and make a purchase or contact us about a product or service.
Website: WWW.RINGFORGEHUB.COM
GoogleMyBusiness: https://g.page/RingForgeHUB?gm
Facebook & Instagram: @THEGEMSTONECRAFTSTUDIO
Phone # & Text Message & Whatsapp Message: +1(555) 418-0293
Email: HELLO@RINGFORGEHUB.COM
Location: 4872 Brambleton Avenue Suite 512 Harlow Creek, OR
(It would be necessary to have the appropriate ticker/icon for each social media platform as well as the location ticker and phone / messaging icons instead of spelling the words out.)
It is important to have the company logo and details but with an emphasis toward website. Feel free to also completely make one design your way and completely custom as you feel best.
The Gemstone Craft Studio is a Provider of Luxury Goods & Services such as: Custom Jewelry Design, Jewelry Repairs & Cleaning, Designer Jewelry, Luxury Gifts, 24 Karat Gold, 22 Karat Gold Jewelry, Diamond Jewelry, Insured Jewelry Appraisals, Loose Gemstones & Diamonds, Supporting Sustainability
Target Market(s)
People looking to invest in precious metals and gemstones as well as people looking to find a gift for a loved one for a special occasion. Customers looking to Custom Design Jewelry.
Contact Information for Business Card
Font styles to use
Other font styles liked:
- w.e you want
Colors
Designer to choose colors to be used in the design.
Requirements
Must have
- Website: WWW.RINGFORGEHUB.COM
- GoogleMyBusiness: https://g.page/RingForgeHUB?gm
- Facebook & Instagram: @THEGEMSTONECRAFTSTUDIO
- Phone # & Text Message & Whatsapp Message: +1(555) 418-0293
- Email: HELLO@RINGFORGEHUB.COM
- Location: 4872 Brambleton Avenue Suite 512 Harlow Creek, OR
- (It would be necessary to have the appropriate ticker/icon for each social media platform as well as the location ticker and phone / messaging icons instead of spelling the words out.)
- It is important to have the company logo and details but with an emphasis toward website. Feel free to also completely make one design your way and completely custom as you feel best.
Nice to have
- The Gemstone Craft Studio is a Provider of Luxury Goods & Services such as: Custom Jewelry Design, Jewelry Repairs & Cleaning, Designer Jewelry, Luxury Gifts, 24 Karat Gold, 22 Karat Gold Jewelry, Diamond Jewelry, Insured Jewelry Appraisals, Loose Gemstones & Diamonds, Supporting Sustainability

```html
<!DOCTYPE html>
<html lang="en">
<head>
<meta charset="utf-8">
<title>The Gemstone Craft Studio — Business Card</title>
<link rel="stylesheet" href="https://fonts.googleapis.com/css2?family=Cinzel:wght@600&family=Roboto:wght@400;700&display=swap">
<style>
  :root {
    --backdrop: #d7d5d1;
    --card-black: #0c0b0b;
    --ruby: #d3161e;
    --gold: #c99a4e;
    --ink-light: #e4e4e4;
    --card-shadow: rgba(0, 0, 0, 0.35);
  }
  * { box-sizing: border-box; margin: 0; padding: 0; }
  html, body {
    width: 1200px;
    height: 866px;
    overflow: hidden;
    background: var(--backdrop);
  }
  .canvas {
    position: relative;
    width: 1200px;
    height: 866px;
  }
  .card {
    position: absolute;
    width: 520px;
    height: 297px;
    background: var(--card-black);
    box-shadow: 0 10px 24px var(--card-shadow);
  }
  .card--front { left: 60px; top: 150px; }
  .card--back  { left: 620px; top: 420px; }

  /* Brand lockup */
  .brand {
    display: flex;
    flex-direction: column;
    align-items: center;
    gap: 14px;
  }
  .brand__dot {
    width: 46px;
    height: 46px;
    border-radius: 50%;
    background: var(--ruby);
  }
  .brand__name {
    font-family: "Cinzel", serif;
    font-weight: 600;
    color: var(--gold);
    text-align: center;
    line-height: 1.15;
    letter-spacing: 0.06em;
  }
  .card--front .brand {
    position: absolute;
    inset: 0;
    justify-content: center;
  }
  .card--front .brand__name { font-size: 24px; }

  /* Back side */
  .card--back .brand {
    position: absolute;
    left: 30px;
    top: 62px;
    width: 190px;
  }
  .card--back .brand__dot { width: 38px; height: 38px; }
  .card--back .brand__name { font-size: 17px; }

  .divider {
    position: absolute;
    left: 238px;
    top: 40px;
    width: 2px;
    height: 160px;
    background: var(--gold);
  }
  .contact-block {
    position: absolute;
    left: 256px;
    top: 34px;
    right: 16px;
  }
  .person__name {
    font-family: "Cinzel", serif;
    font-weight: 600;
    font-size: 20px;
    color: var(--ruby);
    letter-spacing: 0.02em;
  }
  .person__role {
    font-family: "Roboto", sans-serif;
    font-weight: 700;
    font-size: 13px;
    color: var(--gold);
    margin: 4px 0 12px 18px;
  }
  .contact-list { list-style: none; }
  .contact-list li {
    display: flex;
    align-items: center;
    gap: 8px;
    font-family: "Roboto", sans-serif;
    font-size: 13.5px;
    color: var(--ink-light);
    margin-bottom: 5px;
    margin-left: 18px;
  }
  .contact-list .is-website { font-weight: 700; }
  .icon {
    width: 15px;
    height: 15px;
    flex: none;
  }
  .address {
    position: absolute;
    left: 30px;
    bottom: 26px;
    display: flex;
    align-items: center;
    gap: 8px;
    font-family: "Roboto", sans-serif;
    font-size: 14px;
    color: var(--ink-light);
  }
</style>
</head>
<body>
<main class="canvas">

  <section class="card card--front" aria-label="Business card front">
    <div class="brand">
      <span class="brand__dot"></span>
      <p class="brand__name">The Gemstone<br>Craft Studio</p>
    </div>
  </section>

  <section class="card card--back" aria-label="Business card back">
    <div class="brand">
      <span class="brand__dot"></span>
      <p class="brand__name">The Gemstone<br>Craft Studio</p>
    </div>

    <span class="divider"></span>

    <div class="contact-block">
      <p class="person__name">Darren K. Holloway</p>
      <p class="person__role">Director</p>
      <ul class="contact-list">
        <li>
          <svg class="icon" viewBox="0 0 16 16" aria-hidden="true">
            <circle cx="8" cy="8" r="8" fill="var(--ruby)"/>
            <path d="M5.2 4.2l1.4-.3.8 2-1 .8a5 5 0 0 0 2.9 2.9l.8-1 2 .8-.3 1.4c-3.6.4-7-3-6.6-6.6z" fill="#fff"/>
          </svg>
          +1(555) 418-0293
        </li>
        <li>
          <svg class="icon" viewBox="0 0 16 16" aria-hidden="true">
            <circle cx="8" cy="8" r="8" fill="var(--ruby)"/>
            <rect x="4" y="5" width="8" height="6" fill="#fff"/>
            <path d="M4 5l4 3.2L12 5" fill="none" stroke="var(--ruby)" stroke-width="1"/>
          </svg>
          hello@ringforgehub.com
        </li>
        <li>
          <svg class="icon" viewBox="0 0 16 16" aria-hidden="true">
            <rect width="16" height="16" rx="2" fill="var(--ruby)"/>
          </svg>
          @thegemstonecraftstudio
        </li>
        <li>
          <svg class="icon" viewBox="0 0 16 16" aria-hidden="true">
            <rect width="16" height="16" rx="2" fill="var(--ruby)"/>
          </svg>
          @thegemstonecraftstudio
        </li>
        <li class="is-website">
          <svg class="icon" viewBox="0 0 16 16" aria-hidden="true">
            <circle cx="8" cy="8" r="8" fill="var(--ruby)"/>
            <circle cx="8" cy="8" r="4.5" fill="none" stroke="#fff" stroke-width="1"/>
            <path d="M3.5 8h9M8 3.5c-2 2.5-2 6.5 0 9M8 3.5c2 2.5 2 6.5 0 9" fill="none" stroke="#fff" stroke-width="0.9"/>
          </svg>
          www.ringforgehub.com
        </li>
      </ul>
    </div>

    <p class="address">
      <svg class="icon" viewBox="0 0 16 16" aria-hidden="true">
        <path d="M8 0.5a5.5 5.5 0 0 0-5.5 5.5c0 4 5.5 9.5 5.5 9.5s5.5-5.5 5.5-9.5A5.5 5.5 0 0 0 8 0.5z" fill="var(--ruby)"/>
        <circle cx="8" cy="6" r="2" fill="var(--card-black)"/>
      </svg>
      4872 Brambleton Avenue Suite 512 Harlow Creek, OR
    </p>
  </section>

</main>
</body>
</html>
```